Business Card and Letterhead Design for Public Accounting Firm

Business card and letterhead design for a CPA Firm located in Orange County, CA. We're looking for a modern and professional design utilizing our existing logo. We'd like a clean "less is more" look, but also something that catches the eye. We provide a high level of service to our clients. Open to single or double sided business cards.

Additional info: color numbers on logo
Blue :
R 0
G 83
B 125

#00537D

Silver :

R 154
G 154
B 154

#9A9A9A

Target Market(s)

Businesses and individuals

Industry/Entity Type

Accounting

Contact Information for Business Card

Hewitt Dansby & Mortlake LLP - 4726 Larkspur Hollow Road, Irvine, CA 92614 - (949)382-7146 - hdmledgers.example

Font styles to use
Serif
Sans Serif
Other font styles liked:
• See font file uploaded

Colors
0054AA
0677BA
7BADD7
CADEEF
E8F1F8

Requirements
Nice to have
• Possibly use the font file provided which matches our logo, but adjust to be not in all caps

```html
<!DOCTYPE html>
<html lang="en">
<head>
<meta charset="utf-8">
<title>Hewitt Dansby &amp; Mortlake LLP — Business Card</title>
<link rel="stylesheet" href="https://fonts.googleapis.com/css2?family=Cinzel:wght@400;500&family=Poppins:wght@400;500&display=swap">
<style>
  :root {
    --brand-blue: #00537D;
    --brand-silver: #9A9A9A;
    --backdrop: #c4c4c4;
    --card-white: #ffffff;
    --text-grey: #4a4a4a;
    --rule-grey: #d9d9d9;
    --mark-deep: #0b3f5d;
    --accent-blue: #2b93d6;
    --rule-deep: #0a4564;
  }
  * { margin: 0; padding: 0; box-sizing: border-box; }
  html, body {
    width: 1093px; height: 1200px; overflow: hidden;
    background: var(--backdrop);
  }
  .sheet { position: relative; width: 1093px; height: 1200px; }
  .card {
    position: absolute; left: 265px; width: 578px; height: 356px;
    border-radius: 27px; overflow: hidden;
  }
  .card--front { top: 226px; background: var(--card-white); }
  .card--back { top: 621px; background: var(--brand-blue); }

  .front__mark {
    position: absolute; left: 0; width: 281px; top: 150px;
    text-align: center;
    font-family: "Cinzel", serif; font-weight: 400; font-size: 50px;
    color: var(--brand-blue); line-height: 1;
  }
  .front__rule {
    position: absolute; left: 281px; top: 74px; width: 1px; height: 208px;
    background: var(--rule-grey);
  }
  .front__details {
    position: absolute; left: 305px; top: 88px;
    font-family: "Poppins", sans-serif; color: var(--text-grey);
  }
  .person__name {
    font-family: "Cinzel", serif; font-weight: 500; font-size: 21px;
    color: var(--brand-blue); line-height: 24px; letter-spacing: 0.2px;
  }
  .person__title { font-size: 16px; line-height: 18px; }
  .contact { margin-top: 18px; list-style: none; }
  .contact__item {
    display: flex; align-items: center; gap: 7px;
    font-size: 17px; line-height: 22px;
  }
  .contact__item svg { width: 15px; height: 15px; flex: none; }
  .contact__web { color: var(--brand-blue); }
  .firm { margin-top: 15px; font-size: 16.5px; line-height: 21px; font-style: normal; }
  .firm__name { color: var(--brand-blue); font-weight: 500; }

  .back__mark {
    position: absolute; left: 100px; width: 160px; top: 152px;
    text-align: center;
    font-family: "Cinzel", serif; font-weight: 400; font-size: 44px;
    color: var(--mark-deep); line-height: 1;
  }
  .back__rule {
    position: absolute; left: 265px; top: 141px; width: 1px; height: 74px;
    background: var(--rule-deep);
  }
  .back__name {
    position: absolute; left: 277px; top: 151px;
    font-family: "Cinzel", serif; font-weight: 400; font-size: 21px;
    letter-spacing: 3px; line-height: 26px; color: var(--accent-blue);
  }
</style>
</head>
<body>
<main class="sheet">
  <section class="card card--front" aria-label="Business card front">
    <div class="front__mark">HD&amp;M</div>
    <div class="front__rule"></div>
    <div class="front__details">
      <h1 class="person__name">MARCUS ELLERY</h1>
      <p class="person__title">Managing Director</p>
      <ul class="contact">
        <li class="contact__item">
          <svg viewBox="0 0 24 24" aria-hidden="true"><path fill="none" stroke="#00537D" stroke-width="2.4" stroke-linecap="round" stroke-linejoin="round" d="M5 3h4l2 5-2.5 1.5a11 11 0 0 0 6 6L16 13l5 2v4a2 2 0 0 1-2 2A16 16 0 0 1 3 5a2 2 0 0 1 2-2z M14 3a7 7 0 0 1 7 7 M14 7a3 3 0 0 1 3 3"/></svg>
          <span>(949)382-7146</span>
        </li>
        <li class="contact__item">
          <svg viewBox="0 0 24 24" aria-hidden="true"><g fill="none" stroke="#00537D" stroke-width="2"><circle cx="12" cy="12" r="10"/><ellipse cx="12" cy="12" rx="4" ry="10"/><path d="M2 12h20M4 7h16M4 17h16"/></g></svg>
          <span>www.<span class="contact__web">hdmledgers.example</span></span>
        </li>
      </ul>
      <address class="firm">
        <span class="firm__name">Hewitt Dansby &amp; Mortlake LLP</span><br>
        4726 Larkspur Hollow Road,<br>
        Irvine, CA 92614
      </address>
    </div>
  </section>

  <section class="card card--back" aria-label="Business card back">
    <div class="back__mark">HD&amp;M</div>
    <div class="back__rule"></div>
    <p class="back__name">HEWITT DANSBY<br>&amp; MORTLAKE LLP</p>
  </section>
</main>
</body>
</html>
```